Brightfern IT Solutions Web Design

We are a new business in Perth Australia specializing in supporting Home residential and Small business with their IT requirements
We believe image and presentation is important and having a eye catching, professional, intuitive website is a must.
Although we are still expanding as business the message we would like to convey to users is that they can trust our work.

Services we provide are
Please refer to text file attached

Future services
- Email hosting
- Domain resller
- Cloud services

A wordpress theme i really like is below.
http://www.quillmarket-example.com/site-themes/58314.html
Orange colour included is a preference however a colour that goes withg my logo is fine too.

The logo i would like to include is also attached.

I would like the web site design to be built and coded in wordpress and handed over to me so i can continue updating the content, source will be require.

Target Market(s)

Home residential and Small business users

Industry/Entity Type

Residential

Requirements
Must have
• The form to email function in the contact us page.
Nice to have
• Interactive icons

```html
<!DOCTYPE html>
<html lang="en">
<head>
<meta charset="utf-8">
<title>Brightfern IT Solutions</title>
<link rel="stylesheet" href="https://fonts.googleapis.com/css2?family=Roboto:wght@300;400;500;700&display=swap">
<style>
  :root{
    --orange:#f7862a;
    --orange-light:#fa9a4a;
    --red:#f2452a;
    --ink:#333538;
    --ink-dark:#3a3c40;
    --text:#555;
    --muted:#8a8a8a;
    --card:#f2f2f2;
    --line:#e2e2e2;
    --white:#fff;
    --header:#f4f4f4;
  }
  *{box-sizing:border-box;margin:0;padding:0}
  html,body{width:757px;height:1200px;overflow:hidden;background:var(--white)}
  body{position:relative;font-family:"Roboto",Arial,sans-serif;color:var(--text)}
  .abs{position:absolute}

  /* header */
  .site-header{left:0;top:0;width:757px;height:47px;background:var(--header);border-bottom:1px solid #ddd}
  .brand{left:47px;top:8px;width:180px;display:flex;align-items:center;gap:8px}
  .brand-mark{width:28px;height:28px;background:var(--orange);flex:none}
  .brand-name{font-size:13px;line-height:14px;font-weight:700;color:var(--ink);letter-spacing:1px}
  .nav-item{top:0;height:47px;display:flex;align-items:center;justify-content:center;font-size:7.5px;font-weight:500;color:var(--ink);border-left:1px solid #e0e0e0;letter-spacing:.3px;flex-direction:column}
  .nav-item .caret{width:0;height:0;border-left:2.5px solid transparent;border-right:2.5px solid transparent;border-top:3px solid var(--ink);margin-top:4px}
  .cart-count{left:612px;top:4px;width:13px;height:13px;border:1px solid #888;border-radius:50%;font-size:7px;display:flex;align-items:center;justify-content:center;color:var(--ink)}
  .signup{left:645px;top:13px;width:54px;height:23px;background:var(--orange);color:var(--white);font-size:7px;font-weight:500;display:flex;align-items:center;justify-content:center;border-radius:2px}
  .corner{right:0;top:0}

  /* hero */
  .hero{left:0;top:47px;width:757px;height:307px;background:linear-gradient(100deg,#3c3e42 0%,#2b2d30 45%,#3a3c40 100%)}
  .hero-server{left:478px;top:80px;width:218px;height:240px;background:radial-gradient(ellipse at 45% 50%,#4a4d4f 0%,#2f3133 60%,transparent 72%)}
  .hero-title{left:59px;top:121px;font-size:25px;font-weight:400;color:var(--white);line-height:31px}
  .hero-title em{font-style:normal;font-weight:500;color:var(--red)}
  .hero-sub{left:59px;top:189px;font-size:12px;color:var(--white);font-weight:300}
  .hero-list{left:59px;top:212px;list-style:none}
  .hero-list li{display:flex;align-items:center;gap:9px;font-size:8px;color:var(--white);height:22.5px}
  .star{width:13px;height:13px;border-radius:50%;background:var(--red);display:flex;align-items:center;justify-content:center}
  .btn-outline{border:1px solid var(--white);color:var(--white);font-size:7px;display:flex;align-items:center;justify-content:center;font-weight:500}
  .learn{left:59px;top:289px;width:71px;height:22px}
  .price-label{left:143px;top:282px;font-size:12px;color:var(--white);font-weight:300}
  .price{left:143px;top:296px;font-size:19px;color:var(--red);font-weight:400}

  /* band */
  .band{left:0;top:357px;width:757px;height:64px;background:var(--orange)}
  .band-title{left:59px;top:368px;font-size:17px;color:var(--white);font-weight:400}
  .band-sub{left:59px;top:390px;font-size:8px;color:#fff6ee}
  .band-btn{left:625px;top:375px;width:74px;height:23px}

  /* features */
  .feature{top:485px;width:200px}
  .feature-icon{width:30px;height:30px;border-radius:50%;background:var(--ink-dark);display:flex;align-items:center;justify-content:center}
  .feature-title{position:absolute;left:43px;top:8px;font-size:11px;color:var(--ink);font-weight:400}
  .feature-text{margin-top:24px;font-size:7.3px;line-height:14.5px;color:var(--muted)}

  /* domain */
  .domain{left:2px;top:613px;width:755px;height:240px;background:linear-gradient(120deg,#8e9396 0%,#b7bbbd 45%,#9da2a5 70%,#7a7f82 100%)}
  .domain-title{left:0;width:757px;top:666px;text-align:center;font-size:17px;color:var(--white);font-weight:300}
  .domain-sub{left:0;width:757px;top:691px;text-align:center;font-size:9.5px;color:#eee;font-weight:300}
  .www{left:144px;top:721px;font-size:9px;color:var(--white)}
  .domain-input{left:168px;top:714px;width:398px;height:24px;background:rgba(255,255,255,.28);border:1px solid rgba(255,255,255,.4)}
  .domain-search{left:566px;top:714px;width:68px;height:24px;background:var(--red);display:flex;align-items:center;justify-content:center}
  .domain-hint{left:0;width:757px;top:742px;text-align:center;font-size:7px;color:var(--white)}
  .tld-row{left:248px;top:759px;width:266px;height:21px;display:flex;border:1px solid rgba(255,255,255,.35)}
  .tld{flex:1;display:flex;align-items:center;gap:3px;padding-left:4px;font-size:7px;color:var(--white);border-right:1px solid rgba(255,255,255,.35)}
  .tld:last-child{border-right:0}
  .tld i{width:7px;height:7px;border:1px solid var(--white);background:rgba(255,255,255,.2)}

  /* pricing */
  .plan{top:927px;width:147px;height:260px;background:var(--card);text-align:center}
  .plan.featured{background:var(--orange)}
  .plan-price{position:absolute;left:45.5px;top:-28px;width:56px;height:56px;border-radius:50%;background:var(--ink-dark);color:var(--white);display:flex;flex-direction:column;align-items:center;justify-content:center}
  .featured .plan-price{background:var(--orange);border:2px solid var(--white)}
  .plan-price b{font-size:16px;font-weight:300;line-height:17px}
  .plan-price small{font-size:6px}
  .plan-name{position:absolute;left:0;width:100%;top:43px;font-size:8.5px;font-weight:700;color:var(--ink)}
  .featured .plan-name{color:var(--white)}
  .plan-features{position:absolute;left:12px;right:12px;top:65px;list-style:none}
  .plan-features li{height:27.5px;display:flex;align-items:center;justify-content:center;font-size:7px;color:#666;border-bottom:1px solid var(--line)}
  .plan-features li:last-child{border-bottom:0}
  .featured .plan-features li{color:var(--white);border-bottom-color:rgba(255,255,255,.3)}
  .plan-btn{position:absolute;left:32px;top:217px;width:83px;height:23px;background:var(--ink-dark);color:var(--white);font-size:7px;display:flex;align-items:center;justify-content:center}
  .featured .plan-btn{background:var(--orange-light)}
</style>
</head>
<body>

<header class="site-header abs">
  <div class="brand abs"><span class="brand-mark"></span><span class="brand-name">BRIGHTFERN<br>IT SOLUTIONS</span></div>
  <div class="nav-item abs" style="left:243px;width:45px">HOME<span class="caret"></span></div>
  <div class="nav-item abs" style="left:288px;width:45px">PAGES<span class="caret"></span></div>
  <div class="nav-item abs" style="left:333px;width:72px">SHORTCODES<span class="caret"></span></div>
  <div class="nav-item abs" style="left:405px;width:49px">CLIENTS<span class="caret"></span></div>
  <div class="nav-item abs" style="left:454px;width:60px">FEATURES<span class="caret"></span></div>
  <div class="nav-item abs" style="left:514px;width:42px">SHOP<span class="caret"></span></div>
  <div class="nav-item abs" style="left:556px;width:43px">BLOG</div>
  <div class="nav-item abs" style="left:599px;width:35px;border-right:1px solid #e0e0e0">
    <svg width="10" height="9" viewBox="0 0 10 9"><path d="M0 1h2l1.5 5h5L10 2.5H3" fill="none" stroke="#333" stroke-width="1.2"/><circle cx="4" cy="8" r="1" fill="#333"/><circle cx="8" cy="8" r="1" fill="#333"/></svg>
  </div>
  <div class="cart-count abs">0</div>
  <div class="signup abs">&#9679;&nbsp;SIGN UP</div>
  <svg class="corner abs" width="14" height="14" viewBox="0 0 14 14"><path d="M0 0h14v14z" fill="var(--orange)"/></svg>
</header>

<section class="hero abs" role="img" aria-label="Dark photo of a glass office tower seen from below"></section>
<div class="hero-server abs" role="img" aria-label="Photo of black rack server units with green drive bays"></div>
<h1 class="hero-title abs">Build <em>your dream</em> website with<br>cloud hosting</h1>
<p class="hero-sub abs">A complete website solution for your business or personal website</p>
<ul class="hero-list abs">
  <li><span class="star"><svg width="7" height="7" viewBox="0 0 10 10"><path d="M5 0l1.5 3.3 3.5.3-2.7 2.3.9 3.6L5 7.6 1.8 9.5l.9-3.6L0 3.6l3.5-.3z" fill="#fff"/></svg></span>Intuitive editor</li>
  <li><span class="star"><svg width="7" height="7" viewBox="0 0 10 10"><path d="M5 0l1.5 3.3 3.5.3-2.7 2.3.9 3.6L5 7.6 1.8 9.5l.9-3.6L0 3.6l3.5-.3z" fill="#fff"/></svg></span>40+ professional templates</li>
  <li><span class="star"><svg width="7" height="7" viewBox="0 0 10 10"><path d="M5 0l1.5 3.3 3.5.3-2.7 2.3.9 3.6L5 7.6 1.8 9.5l.9-3.6L0 3.6l3.5-.3z" fill="#fff"/></svg></span>Customisable &amp; responsive designs</li>
</ul>
<div class="btn-outline learn abs">LEARN MORE</div>
<div class="price-label abs">Starting at</div>
<div class="price abs">£2.99/mo</div>

<section class="band abs"></section>
<h2 class="band-title abs">Managed Dedicated Servers</h2>
<p class="band-sub abs">Blazing performance, supreme flexibility &amp; superior UK based support.</p>
<div class="btn-outline band-btn abs">GET STARTED</div>

<div class="feature abs" style="left:59px">
  <div class="feature-icon"><svg width="12" height="12" viewBox="0 0 12 12"><path d="M2 10l6-6M8 1v2M10 3h2M9 1.5l1.5 1.5" stroke="#fff" stroke-width="1.4" fill="none"/></svg></div>
  <h3 class="feature-title">Backups Available</h3>
  <p class="feature-text">Compellingly transform plug-and-play expertise whereas efficient platforms. Authoritatively communicate quality sources vis-a-vis standards compliant partnerships.</p>
</div>
<div class="feature abs" style="left:278px">
  <div class="feature-icon"><svg width="14" height="12" viewBox="0 0 14 12"><circle cx="7" cy="3.5" r="3" fill="none" stroke="#fff" stroke-width="1.3"/><circle cx="3.5" cy="8.5" r="3" fill="none" stroke="#fff" stroke-width="1.3"/><circle cx="10.5" cy="8.5" r="3" fill="none" stroke="#fff" stroke-width="1.3"/></svg></div>
  <h3 class="feature-title">Reliable Hardware</h3>
  <p class="feature-text">Compellingly transform plug-and-play expertise whereas efficient platforms. Authoritatively communicate quality sources vis-a-vis standards compliant partnerships.</p>
</div>
<div class="feature abs" style="left:497px">
  <div class="feature-icon"><svg width="12" height="12" viewBox="0 0 12 12"><path d="M1 11C1 5 5 1 11 1c0 6-4 10-10 10zM1 11l6-6" stroke="#fff" stroke-width="1.3" fill="none"/></svg></div>
  <h3 class="feature-title">99.99% Uptime</h3>
  <p class="feature-text">Compellingly transform plug-and-play expertise whereas efficient platforms. Authoritatively communicate quality sources vis-a-vis standards compliant partnerships.</p>
</div>

<section class="domain abs" role="img" aria-label="Faded photo of business people meeting around a table"></section>
<h2 class="domain-title abs">Get the domain of your dreams</h2>
<p class="domain-sub abs">Starting from as little as £3.35 per year!</p>
<span class="www abs">www.</span>
<div class="domain-input abs"></div>
<div class="domain-search abs"><svg width="12" height="12" viewBox="0 0 12 12"><circle cx="5" cy="5" r="3.6" fill="none" stroke="#fff" stroke-width="1.8"/><path d="M7.6 7.6L11 11" stroke="#fff" stroke-width="2"/></svg></div>
<p class="domain-hint abs">(e.g yourcompany)</p>
<div class="tld-row abs">
  <span class="tld"><i></i>.com</span>
  <span class="tld"><i></i>.net</span>
  <span class="tld"><i></i>.org</span>
  <span class="tld"><i></i>.co</span>
</div>

<div class="plan abs" style="left:59px">
  <div class="plan-price"><b>$20</b><small>pm</small></div>
  <h3 class="plan-name">BASIC PLAN</h3>
  <ul class="plan-features"><li>10GB Storage Space</li><li>50GB Bandwidth</li><li>10 Free Sub-Domains</li><li>100 E-mail Accounts</li><li>Control Panel &amp; FTP</li></ul>
  <div class="plan-btn">GET STARTED</div>
</div>
<div class="plan abs" style="left:223px">
  <div class="plan-price"><b>$30</b><small>pm</small></div>
  <h3 class="plan-name">PREMIUM PLAN</h3>
  <ul class="plan-features"><li>10GB Storage Space</li><li>50GB Bandwidth</li><li>10 Free Sub-Domains</li><li>100 E-mail Accounts</li><li>Control Panel &amp; FTP</li></ul>
  <div class="plan-btn">GET STARTED</div>
</div>
<div class="plan featured abs" style="left:387px">
  <div class="plan-price"><b>$50</b><small>pm</small></div>
  <h3 class="plan-name">ADVANCE PLAN</h3>
  <ul class="plan-features"><li>10GB Storage Space</li><li>50GB Bandwidth</li><li>10 Free Sub-Domains</li><li>100 E-mail Accounts</li><li>Control Panel &amp; FTP</li></ul>
  <div class="plan-btn">GET STARTED</div>
</div>
<div class="plan abs" style="left:551px">
  <div class="plan-price"><b>$20</b><small>pm</small></div>
  <h3 class="plan-name">BASIC PLAN</h3>
  <ul class="plan-features"><li>10GB Storage Space</li><li>50GB Bandwidth</li><li>10 Free Sub-Domains</li><li>100 E-mail Accounts</li><li>Control Panel &amp; FTP</li></ul>
  <div class="plan-btn">GET STARTED</div>
</div>

</body>
</html>
```